Webdesign für Kfz-Betrieb
Zielgruppe
Seit über 20 Jahren ist Radwerk Olbertz die erste Anlaufstelle wenn es um die Themen Reifen, Felgen und den gesamten Kfz-Bereich geht. Außerdem ist das Unternehmen seit 1997 auf Fahrzeugaufbereitung spezialisiert.
ZG: Alle, die Reifen benötigen
Aufgabenstellung
Layout Adobe Photoshop
hell, freundlich, aufgeschlossen
Die Leistungen sollen mit Icons dargestellt werden. (siehe Welche Inhalte sollen angezeigt werden)
Logo liegt noch nicht vor
nur die Startseite layouten

```html
<!DOCTYPE html>
<html lang="de">
<head>
<meta charset="utf-8">
<title>Radwerk Olbertz – Startseite</title>
<link href="https://fonts.googleapis.com/css2?family=Arimo:ital,wght@0,400;0,500;0,700;1,400&display=swap" rel="stylesheet">
<style>
:root{
  --green:#107a14;
  --green-dark:#0b6510;
  --mint:#cfe3cf;
  --ink:#1d1d1b;
  --text:#333;
  --grey-bg:#f5f5f5;
  --white:#fff;
  --placeholder:#a8a8a8;
}
*{margin:0;padding:0;box-sizing:border-box}
html,body{width:1200px;height:3396px;overflow:hidden}
body{position:relative;background:var(--white);font-family:"Arimo",Arial,sans-serif;color:var(--ink)}
.abs{position:absolute}

/* header */
.brand{left:0;width:1200px;top:22px;display:flex;justify-content:center;align-items:center;gap:12px}
.brand-dot{width:30px;height:30px;border-radius:50%;background:var(--green)}
.brand-name{font-size:38px;font-weight:700;color:var(--green);letter-spacing:-.5px}
.main-nav{top:94px;left:104px;width:992px;display:flex;justify-content:space-between;font-size:13.5px;font-weight:500;letter-spacing:.2px}

/* hero */
.hero{top:125px;left:0;width:1200px;height:571px;
  background:linear-gradient(100deg,#c8301d 0%,#e0432a 22%,#3a3a38 38%,#8a8a80 55%,#6f7e58 75%,#4d6236 100%)}
.hero-title{top:272px;left:200px;width:800px;text-align:center;color:var(--white);font-size:50px;font-weight:700;line-height:61px;text-shadow:0 2px 8px rgba(0,0,0,.35)}

/* green panels */
.panel{background:var(--green);color:var(--white)}
.panel-title{font-size:23px;font-weight:500;letter-spacing:.2px}
.label{font-size:12px;font-weight:500}
.field{background:var(--white);border-radius:3px;height:30px;font-size:12px;font-style:italic;color:var(--placeholder);padding:0 8px;display:flex;align-items:center;justify-content:space-between}
.caret{width:0;height:0;border-left:6px solid transparent;border-right:6px solid transparent;border-top:6px solid #888;font-style:normal}
.btn-outline{border:2px solid var(--white);border-radius:8px;color:var(--white);font-size:15px;font-weight:500;display:flex;align-items:center;justify-content:center}
.small{font-size:10.5px;line-height:13px;color:#e6f1e6}

/* headings */
.section-heading{left:0;width:1200px;text-align:center;font-size:23px;font-weight:500;letter-spacing:.5px;color:#2a2a2a}
.heading-rule{height:1px;background:var(--green)}

/* services */
.service{width:200px;text-align:center}
.service-icon{width:156px;height:156px;border-radius:50%;background:var(--mint);margin:0 auto;display:flex;align-items:center;justify-content:center}
.service-label{margin-top:28px;font-size:12.5px;font-weight:500;letter-spacing:.2px}

/* feature blocks */
.grey-band{left:0;width:1200px;background:var(--grey-bg)}
.photo{border-radius:0}
.feature-title{font-size:24px;font-weight:500;color:var(--green);letter-spacing:.3px}
.feature-text{font-size:14.5px;line-height:25px;color:var(--text)}
.btn-green{border:2px solid var(--green);border-radius:5px;color:var(--green);font-size:15px;font-weight:500;display:flex;align-items:center;justify-content:center;background:var(--white)}

.company-text{left:176px;width:848px;text-align:center;font-size:14.5px;line-height:25px;color:var(--text)}

.dot{width:18px;height:18px;border-radius:50%;border:2px solid var(--green)}
.dot.active{background:var(--green)}

.footer{left:0;width:1200px;font-size:11px;color:#555;text-align:center;line-height:14px}
</style>
</head>
<body>

<header>
  <div class="abs brand"><span class="brand-dot"></span><span class="brand-name">Radwerk Olbertz</span></div>
  <nav class="abs main-nav">
    <span>LEISTUNGEN</span><span>TERMINVEREINBARUNG</span><span>UNTERNEHEMEN</span><span>AKTUELLES</span><span>ABVERKAUF</span><span>REIFENVERKAUF</span><span>ENGAGEMENT</span>
  </nav>
</header>

<section>
  <div class="abs hero" role="img" aria-label="Foto: rotes Auto mit Reifen in schneller Fahrt auf einer Landstraße"></div>
  <h1 class="abs hero-title">Ihre nächste Radwerk ist in Lindenau - Service und Kompetenz aus einer Hand.</h1>
</section>

<!-- booking -->
<section class="abs panel" style="left:109px;top:607px;width:968px;height:278px">
  <div class="abs panel-title" style="left:50px;top:22px">TERMINVEREINBARUNG</div>
  <div class="abs label" style="left:51px;top:63px">Dienstleistungen</div>
  <div class="abs field" style="left:51px;top:85px;width:354px">Bitte wählen...<span class="caret"></span></div>

  <svg class="abs" style="left:51px;top:131px" width="20" height="20" viewBox="0 0 20 20"><circle cx="10" cy="10" r="8.5" fill="none" stroke="#fff" stroke-width="1.6"/><path d="M10 5v5l3 2" fill="none" stroke="#fff" stroke-width="1.6" stroke-linecap="round"/></svg>
  <div class="abs label" style="left:80px;top:135px;font-size:11px">Ihr nächstmöglicher Werkstatttermin</div>
  <div class="abs small" style="left:51px;top:160px">Mittwoch, 18. September 2022 08:00 Uhr</div>
  <div class="abs small" style="left:51px;top:181px;width:210px">Sie können den Werkstatttermin später im Buchungsprozess noch anpassen.</div>

  <svg class="abs" style="left:291px;top:130px" width="16" height="22" viewBox="0 0 16 22"><path d="M8 0C3.6 0 0 3.5 0 7.9 0 13.5 8 22 8 22s8-8.5 8-14.1C16 3.5 12.4 0 8 0z" fill="#fff"/><circle cx="8" cy="8" r="3" fill="var(--green)"/></svg>
  <div class="abs label" style="left:316px;top:135px;font-size:11px">Ihre Werkstatt</div>
  <div class="abs small" style="left:291px;top:163px">Radwerk Olbertz<br>Mühlgasse 12<br>04567 Lindenau</div>

  <div class="abs label" style="left:509px;top:63px">Kontakt</div>
  <div class="abs field" style="left:509px;top:85px;width:186px">Nachname</div>
  <div class="abs field" style="left:732px;top:85px;width:187px">PLZ/Ort</div>
  <div class="abs field" style="left:509px;top:129px;width:186px">Vorname</div>
  <div class="abs field" style="left:732px;top:129px;width:187px">Rückrufnummer</div>
  <div class="abs field" style="left:509px;top:171px;width:186px">Straße</div>
  <div class="abs field" style="left:732px;top:171px;width:187px">Email</div>

  <div class="abs btn-outline" style="left:418px;top:224px;width:147px;height:29px">Weiter</div>
</section>

<!-- services -->
<section>
  <h2 class="abs section-heading" style="top:943px">UNSERE LEISTUNGEN</h2>
  <div class="abs heading-rule" style="left:500px;top:976px;width:200px"></div>

  <div class="abs service" style="left:99px;top:1016px">
    <div class="service-icon"><svg width="90" height="90" viewBox="0 0 90 90" fill="none" stroke="var(--green)" stroke-width="3.5"><rect x="32" y="12" width="46" height="14" rx="4"/><rect x="32" y="66" width="46" height="14" rx="4"/><circle cx="33" cy="50" r="24"/><circle cx="33" cy="50" r="12"/><circle cx="33" cy="50" r="3"/><path d="M33 26v12M33 62v12M9 50h12M45 50h12"/></svg></div>
    <div class="service-label">EINLAGERUNG</div>
  </div>
  <div class="abs service" style="left:300px;top:1016px">
    <div class="service-icon"><svg width="90" height="90" viewBox="0 0 90 90" fill="none" stroke="var(--green)" stroke-width="3.5"><rect x="12" y="10" width="38" height="62" rx="3"/><rect x="23" y="5" width="16" height="9" rx="2"/><path d="M20 26h6M30 26h14M20 38h6M30 38h14M20 50h6M30 50h14"/><path d="M50 46h20l10 14v14H50z"/><circle cx="58" cy="76" r="5"/><circle cx="74" cy="76" r="5"/></svg></div>
    <div class="service-label">FAHRZEUGAUFBEREITUNG</div>
  </div>
  <div class="abs service" style="left:500px;top:1016px">
    <div class="service-icon"><svg width="90" height="90" viewBox="0 0 90 90" fill="none" stroke="var(--green)" stroke-width="3.5"><circle cx="40" cy="36" r="14"/><path d="M34 36l4 4 8-8"/><path d="M40 16v6M40 50v6M20 36h6M54 36h6M26 22l4 4M50 46l4 4M54 22l-4 4"/><path d="M70 10v14l-6 6v40l6 8 6-8V30l-6-6"/><path d="M10 66l6-12h22l6 12v10H10z"/><circle cx="18" cy="78" r="4"/><circle cx="36" cy="78" r="4"/></svg></div>
    <div class="service-label">FAHRZEUGINSPEKTION</div>
  </div>
  <div class="abs service" style="left:699px;top:1016px">
    <div class="service-icon"><svg width="90" height="90" viewBox="0 0 90 90" fill="none" stroke="var(--green)" stroke-width="3.5"><rect x="10" y="22" width="18" height="56" rx="4"/><rect x="28" y="30" width="12" height="40" rx="2"/><path d="M14 32h10M14 42h10M14 52h10M14 62h10"/><path d="M40 52h40v20H40z"/><path d="M44 52c4-6 8-6 12 0 4-6 8-6 12 0 4-6 8-6 12 0"/><path d="M66 14v10M61 19h10M78 30v8M74 34h8"/></svg></div>
    <div class="service-label">RÄDERWÄSCHE</div>
  </div>
  <div class="abs service" style="left:900px;top:1016px">
    <div class="service-icon"><svg width="90" height="90" viewBox="0 0 90 90" fill="none" stroke="var(--green)" stroke-width="3.5"><rect x="12" y="14" width="26" height="66" rx="6"/><path d="M18 24l14 8M18 36l14 8M18 48l14 8M18 60l14 8"/><circle cx="62" cy="30" r="16"/><circle cx="62" cy="30" r="8"/><path d="M62 30l5-5"/><path d="M62 46v16c0 10-10 10-14 10h-10"/></svg></div>
    <div class="service-label">STICKSTOFF-FÜLLUNG</div>
  </div>
</section>

<!-- abverkauf -->
<section>
  <div class="abs grey-band" style="top:1288px;height:648px"></div>
  <div class="abs photo" style="left:109px;top:1328px;width:231px;height:498px;background:linear-gradient(160deg,#5d6670 0%,#8a9098 40%,#4b5a72 70%,#6a6a66 100%)" role="img" aria-label="Foto: Mechaniker montiert ein Rad mit Schlagschrauber"></div>
  <div class="abs photo" style="left:369px;top:1360px;width:231px;height:436px;background:linear-gradient(170deg,#6b7a55 0%,#c9392a 30%,#2c2c2c 50%,#9a9890 75%,#7f7d78 100%)" role="img" aria-label="Foto: rotes Auto in Fahrt, Nahaufnahme des Rades"></div>
  <h2 class="abs feature-title" style="left:642px;top:1381px">ABVERKAUF</h2>
  <p class="abs feature-text" style="left:638px;top:1446px;width:360px">Lorem ipsum dolor sit amet, consetetur sadipscing elitr, sed diam nonumy eirmod tempor invidunt ut labore et dolore magna aliquyam erat, sed diam voluptua. At vero eos et accusam et justo duo dolores et ea rebum. Stet clita kasd gubergren, no sea takimata sanctus est Lorem ipsum dolor sit amet. Lorem ipsum dolor sit amet, consetetur sadipscing elitr, sed diam nonumy eirmod tempor invidunt ut labore et dolore magna aliquyam erat,</p>
  <div class="abs btn-green" style="left:646px;top:1732px;width:137px;height:38px">Mehr</div>
</section>

<!-- tyre finder -->
<section class="abs panel" style="left:109px;top:1863px;width:968px;height:285px">
  <div class="abs panel-title" style="left:50px;top:23px">FINDEN SIE IHREN PASSENDEN REIFEN</div>
  <div class="abs label" style="left:51px;top:76px">Fahrzeug</div>
  <div class="abs label" style="left:358px;top:76px">Saison</div>
  <div class="abs label" style="left:651px;top:76px">Breite</div>
  <div class="abs field" style="left:51px;top:97px;width:267px">Bitte wählen...<span class="caret"></span></div>
  <div class="abs field" style="left:358px;top:97px;width:267px">Bitte wählen...<span class="caret"></span></div>
  <div class="abs field" style="left:651px;top:97px;width:268px">Bitte wählen...<span class="caret"></span></div>
  <div class="abs label" style="left:51px;top:138px">Höhe</div>
  <div class="abs label" style="left:358px;top:138px">Zoll</div>
  <div class="abs label" style="left:651px;top:138px">Marke</div>
  <div class="abs field" style="left:51px;top:160px;width:267px">Bitte wählen...<span class="caret"></span></div>
  <div class="abs field" style="left:358px;top:160px;width:267px">Bitte wählen...<span class="caret"></span></div>
  <div class="abs field" style="left:651px;top:160px;width:268px">Bitte wählen...<span class="caret"></span></div>
  <div class="abs btn-outline" style="left:417px;top:228px;width:148px;height:30px">Reifen finden</div>
</section>

<!-- company -->
<section>
  <h2 class="abs section-heading" style="top:2204px">UNTERNEHMEN</h2>
  <div class="abs heading-rule" style="left:530px;top:2235px;width:140px"></div>
  <p class="abs company-text" style="top:2296px">Lorem ipsum dolor sit amet, consetetur sadipscing elitr, sed diam nonumy eirmod tempor invidunt ut labore et dolore magna aliquyam erat, sed diam voluptua. At vero eos et accusam et justo duo dolores et ea rebum. Stet clita kasd gubergren, no sea takimata sanctus est Lorem ipsum dolor sit amet. Lorem ipsum dolor sit amet, consetetur sadipscing elitr, sed diam nonumy eirmod tempor invidunt ut labore et dolore magna aliquyam erat, sed diam voluptua. At vero eos et accusam et justo duo dolores et ea rebum. Stet clita kasd gubergren, no sea takimata sanctus est Lorem ipsum dolor sit amet.<br>Lorem ipsum dolor sit amet, consetetur sadipscing elitr, sed diam nonumy eirmod tempor invidunt ut labore et dolore magna aliquyam erat, sed diam voluptua. At vero eos et accusam et justo duo dolores et ea rebum. Stet clita kasd gubergren, no sea takimata sanctus est Lorem ipsum dolor sit amet. Lorem ipsum dolor sit amet, consetetur sadipscing</p>
</section>

<!-- lorem ipsum slider + footer -->
<section>
  <div class="abs grey-band" style="top:2615px;height:781px"></div>
  <div class="abs photo" style="left:109px;top:2645px;width:491px;height:499px;background:radial-gradient(circle at 60% 45%,#c99a86 0%,#8c8f94 35%,#5c6a78 70%,#3f4a56 100%)" role="img" aria-label="Foto: Hand mit Schraubenschlüssel und Daumen hoch"></div>
  <h2 class="abs feature-title" style="left:642px;top:2684px">LOREM IPSUM</h2>
  <p class="abs feature-text" style="left:642px;top:2751px;width:360px">Lorem ipsum dolor sit amet, consetetur sadipscing elitr, sed diam nonumy eirmod tempor invidunt ut labore et dolore magna aliquyam erat, sed diam voluptua. At vero eos et accusam et justo duo dolores et ea rebum. Stet clita kasd gubergren, no sea takimata sanctus est Lorem ipsum dolor sit amet. Lorem ipsum dolor sit amet, consetetur sadipscing elitr, sed diam nonumy eirmod tempor invidunt ut labore et dolore magna aliquyam erat, sed diam voluptua. At vero eos et accusam et justo</p>
  <div class="abs btn-green" style="left:646px;top:3069px;width:137px;height:38px">Mehr</div>
  <div class="abs dot active" style="left:562px;top:3185px"></div>
  <div class="abs dot" style="left:591px;top:3185px"></div>
  <div class="abs dot" style="left:619px;top:3185px"></div>

  <footer>
    <div class="abs footer" style="top:3284px;font-weight:500;color:#222">Radwerk Olbertz</div>
    <div class="abs" style="left:513px;top:3308px;font-size:11px;line-height:14px;color:#555">Mühlgasse 12<br>04567 Lindenau</div>
    <div class="abs" style="left:607px;top:3308px;font-size:11px;line-height:14px;color:#555">T: 03421 / 55 20 10<br>F: 03421 / 55 20 11</div>
    <div class="abs footer" style="top:3341px">E: service@radwerk-olbertz.de</div>
    <div class="abs footer" style="top:3376px">© Radwerk Olbertz 2022 | All rights reserved. | Impressum | Datenschutz</div>
  </footer>
</section>

</body>
</html>
```